Modern Innovative Business Card Design

We require a nice, modern, clean business card design, ready for upload to Cardomora. Our company develops online banking software solutions for small financial insitutions. The design should be clean, professional, but yet not "corporate boring". See www.fyrolt.com for an idea of business image and profile. The design should communicate innovation, be modern and fresh, yet look professional and established.

Target Market(s)

Finance industry, bankers, entrepreneurs

Industry/Entity Type

Financial

Contact Information for Business Card

Tobias Wendlerup
CEO

FYROLT BV
Lindenwerf 38
1027 HX Amsterdam
The Netherlands

Phone: +31 20 517 8036
Direct: +31 20 604 1758
Skype: tobias.fyrolt
ceo@fyrolt.com
www.fyrolt.com

Font styles to use
Sans Serif

Requirements
Must have
• Should look clean, modern and professional. File should be ready for upload to cardomora.
Should not have
• Boring standard corporate layout

```html
<!DOCTYPE html>
<html lang="en">
<head>
<meta charset="utf-8">
<title>FYROLT Business Card</title>
<link href="https://fonts.googleapis.com/css2?family=Lato:wght@400;700&display=swap" rel="stylesheet">
<style>
  :root {
    --backdrop: #2b2b2b;
    --card: #f6f6f6;
    --ink: #4a4a4a;
    --ink-dark: #3c3c3c;
    --green: #7cc21e;
    --green-dark: #5f9e12;
    --slate: #555759;
  }
  html, body {
    margin: 0;
    width: 1200px;
    height: 997px;
    overflow: hidden;
    background: var(--backdrop);
    font-family: "Lato", Arial, sans-serif;
  }
  .card {
    position: absolute;
    width: 540px;
    height: 308px;
    background: var(--card);
    box-shadow: 0 18px 40px rgba(0,0,0,.55);
    overflow: hidden;
  }
  .card-back { left: 70px; top: 130px; }
  .card-front { left: 590px; top: 520px; }
  .card-band {
    position: absolute;
    left: 0; bottom: 0;
    width: 540px; height: 70px;
  }
  .wordmark {
    position: absolute;
    margin: 0;
    font-weight: 700;
    color: var(--ink-dark);
    letter-spacing: 4px;
    line-height: 1;
  }
  .card-back .wordmark { left: 0; right: 0; top: 92px; text-align: center; font-size: 58px; }
  .tagline {
    position: absolute;
    left: 0; right: 0; top: 160px;
    text-align: center;
    font-size: 11px;
    font-weight: 700;
    letter-spacing: 1.2px;
    color: var(--ink);
  }
  .tagline-rule {
    position: absolute;
    left: 150px; top: 180px;
    width: 240px; height: 2px;
    background: var(--green);
  }
  .website {
    position: absolute;
    left: 0; right: 0; top: 212px;
    text-align: center;
    font-size: 12px;
    letter-spacing: 3px;
    color: var(--ink);
  }
  .card-front .wordmark { left: 200px; top: 40px; font-size: 54px; }
  .person {
    position: absolute;
    left: 40px; top: 180px;
    width: 230px;
    text-align: center;
  }
  .person-name { margin: 0; font-size: 21px; font-weight: 700; color: var(--green); }
  .person-role { margin: 4px 0 0; font-size: 16px; font-weight: 700; color: var(--ink-dark); }
  .divider {
    position: absolute;
    left: 292px; top: 120px;
    width: 3px; height: 120px;
    background: var(--ink);
  }
  .contact-list {
    position: absolute;
    left: 312px; top: 116px;
    margin: 0; padding: 0;
    list-style: none;
    font-size: 14px;
    font-weight: 700;
    color: var(--ink-dark);
  }
  .contact-list li {
    display: flex;
    align-items: flex-start;
    gap: 10px;
    line-height: 18px;
    margin-bottom: 4px;
  }
  .contact-icon { width: 16px; height: 16px; flex: none; margin-top: 1px; }
</style>
</head>
<body>

<article class="card card-back">
  <h2 class="wordmark">FYROLT</h2>
  <p class="tagline">ONLINE BANKING SOFTWARE SOLUTIONS</p>
  <div class="tagline-rule"></div>
  <p class="website">www.fyrolt.com</p>
  <svg class="card-band" viewBox="0 0 540 70" aria-hidden="true">
    <path d="M0 56 L380 44 Q392 44 396 40 L396 70 L0 70 Z" fill="var(--green)"/>
    <path d="M392 70 Q398 34 428 30 L540 26 L540 70 Z" fill="var(--slate)"/>
  </svg>
</article>

<article class="card card-front">
  <h1 class="wordmark">FYROLT</h1>
  <div class="person">
    <p class="person-name">Tobias Wendlerup</p>
    <p class="person-role">CEO</p>
  </div>
  <div class="divider"></div>
  <ul class="contact-list">
    <li>
      <svg class="contact-icon" viewBox="0 0 16 16"><path d="M2 6 Q8 1 14 6 L12 8 L10 6 L6 6 L4 8 Z M4 9 L12 9 L13 14 L3 14 Z" fill="var(--green)"/></svg>
      +31 20 517 8036
    </li>
    <li>
      <svg class="contact-icon" viewBox="0 0 16 16"><rect x="4" y="1" width="8" height="14" rx="1.5" fill="none" stroke="var(--green)" stroke-width="1.6"/></svg>
      +31 20 604 1758
    </li>
    <li>
      <svg class="contact-icon" viewBox="0 0 16 16"><circle cx="8" cy="8" r="7" fill="var(--green)"/></svg>
      tobias.fyrolt
    </li>
    <li>
      <svg class="contact-icon" viewBox="0 0 16 16"><rect x="1" y="3" width="14" height="10" fill="var(--green)"/><path d="M1 3 L8 9 L15 3" fill="none" stroke="var(--card)" stroke-width="1.4"/></svg>
      ceo@fyrolt.com
    </li>
    <li>
      <svg class="contact-icon" viewBox="0 0 16 16"><path d="M8 1 L15 8 L13 8 L13 15 L3 15 L3 8 L1 8 Z" fill="var(--green)"/></svg>
      <span>Lindenwerf 38, 1027 HX Amsterdam<br>The Netherlands</span>
    </li>
  </ul>
  <svg class="card-band" viewBox="0 0 540 70" aria-hidden="true">
    <path d="M0 56 L380 44 Q392 44 396 40 L396 70 L0 70 Z" fill="var(--green)"/>
    <path d="M392 70 Q398 34 428 30 L540 26 L540 70 Z" fill="var(--slate)"/>
  </svg>
</article>

</body>
</html>
```